Packaging design for Virgin Coconut Oil. 100% pure cold pressed coconut oil

We need a new packaging and label design for our Virgin Coconut Oil product. It is currently marketed in the Philippines as a food supplement. We would like to try marketing it to other Asian countries such as Singapore, Malaysia and Hong Kong. The company has been producing this product since 2004 but now would like to venture into exporting our products overseas.

Would like to see designs with earth, natural "organic" colors. Fresh, Clean and pure look. Our trade mark is "Kestrel Meadow". Its a 100% pure cold pressed virgin coconut oil. All in all, we want to totally repackage our product and re-design the trademark to cater to export markets. Thanks!

Mid to High

Health Product

cadf82
9bcb3b
33b8a4
ffffff
3176b5
3276b5
0592cd
fbed22
fece3e

• Bottle shape design ideas.

```html
<!DOCTYPE html>
<html lang="en">
<head>
<meta charset="utf-8">
<title>Kestrel Meadow Virgin Coconut Oil – Label</title>
<link href="https://fonts.googleapis.com/css2?family=Montserrat:ital,wght@0,600;0,800;0,900;1,700&display=swap" rel="stylesheet">
<style>
  :root {
    --backdrop: #ececee;
    --label-cream: #f3ebde;
    --label-cream-deep: #e6d8c2;
    --leaf-green: #8cbb2c;
    --leaf-green-dark: #5f8e1d;
    --husk-brown: #4a2c1a;
    --white: #ffffff;
  }
  * { margin: 0; padding: 0; box-sizing: border-box; }
  html, body {
    width: 686px;
    height: 1200px;
    overflow: hidden;
    background: var(--backdrop);
    font-family: "Montserrat", Arial, sans-serif;
  }
  .label {
    position: absolute;
    left: 63px;
    top: 160px;
    width: 560px;
    height: 880px;
    background: linear-gradient(160deg, var(--label-cream) 0%, var(--label-cream) 55%, var(--label-cream-deep) 100%);
    overflow: hidden;
  }
  .brand-tab {
    position: absolute;
    left: 194px;
    top: 0;
    width: 172px;
    height: 168px;
    background: var(--leaf-green);
    display: flex;
    align-items: center;
    justify-content: center;
    text-align: center;
  }
  .brand-name {
    color: var(--white);
    font-weight: 600;
    font-size: 22px;
    line-height: 1.35;
    letter-spacing: 1px;
    text-transform: uppercase;
  }
  .product-title {
    position: absolute;
    left: 0;
    top: 218px;
    width: 100%;
    text-align: center;
    font-weight: 900;
    font-size: 76px;
    line-height: 0.98;
    letter-spacing: -1px;
    text-transform: uppercase;
  }
  .product-title .word-brown { color: var(--husk-brown); display: block; }
  .product-title .word-green { color: var(--leaf-green); display: block; }
  .coconut-art {
    position: absolute;
    left: 96px;
    top: 470px;
    width: 368px;
    height: 260px;
    border-radius: 50% / 45%;
    background: radial-gradient(ellipse at 45% 50%, #f7f3ea 0%, #c9d98f 35%, #8cbb2c 60%, #6b4a2a 100%);
  }
  .bottom-band {
    position: absolute;
    left: 0;
    bottom: 0;
    width: 560px;
    height: 150px;
  }
  .claim-natural {
    position: absolute;
    left: 36px;
    bottom: 34px;
    color: var(--white);
    font-weight: 800;
    font-size: 22px;
    line-height: 1.3;
    text-transform: uppercase;
  }
  .claim-approved {
    position: absolute;
    right: 30px;
    bottom: 92px;
    color: var(--husk-brown);
    font-weight: 700;
    font-style: italic;
    font-size: 17px;
    line-height: 1.25;
    text-align: right;
  }
</style>
</head>
<body>
  <main class="label">
    <div class="brand-tab">
      <p class="brand-name">Kestrel<br>Meadow</p>
    </div>

    <h1 class="product-title">
      <span class="word-brown">Virgin</span>
      <span class="word-green">Coconut</span>
      <span class="word-brown">Oil</span>
    </h1>

    <div class="coconut-art" role="img" aria-label="Illustration of green coconuts with one split open showing white flesh, on a palm sprig"></div>

    <svg class="bottom-band" viewBox="0 0 560 150" aria-hidden="true">
      <path d="M0 30 C 140 10, 260 20, 330 60 L 560 60 L 560 150 L 0 150 Z" fill="var(--leaf-green)"/>
      <path d="M0 30 C 140 10, 260 20, 330 60 L 330 72 C 250 36, 140 28, 0 44 Z" fill="var(--leaf-green-dark)" opacity="0.5"/>
    </svg>

    <p class="claim-natural">All Natural<br>Food Supplement</p>
    <p class="claim-approved">Approved<br>Therapeutic<br>Claims</p>
  </main>
</body>
</html>
```